IT-Dienstleister für Projektmanagementsoftware sucht Broschüre im DIN-A4-Format
Zielgruppe
Wir sind ein IT-Dienstleister für Projektmanagementsoftware. Wir installieren, migrieren und entwickeln Software für das Projektmanagement auf Basis von Veltrona Technologien. Unsere Zielgruppe sind mittelständische Unternehmen und große Konzerne. Je komplexer das Projektmanagement in einem Unternehmen, desto eher helfen unsere Lösungen.
Aufgabenstellung
Es soll eine DIN A4 Hochglanz Broschüre für eine Messe entstehen. Wir haben bereits ein Grobkonzept mit Bildauswahl und Texten erstellt. An diesem soll sich orientiert werden. Bezüglich desDesigns, der Anordnung der Texte und Bilder etc. besteht völlige Freiheit. Weitere Orientierung bieten unsere Webseiten hollweckfeist.de und tivonet.de. Die Texte und Screenshots sind teilweise nur Platzhalter und müssen später noch angepasst werden können. Wir benötigen daher unbedingt die Rohdaten des Designs.

```html
<!DOCTYPE html>
<html lang="de">
<head>
<meta charset="utf-8">
<title>Hollweck &amp; Feist – Broschüre Umschlag</title>
<link href="https://fonts.googleapis.com/css2?family=Roboto:wght@300;400;500&display=swap" rel="stylesheet">
<style>
  :root {
    --canvas: #d6d6d9;
    --paper: #eeeeef;
    --ink: #1e1e1e;
    --dark: #1c1c1d;
    --green: #8dc63f;
    --white: #ffffff;
    --muted: #c9c9c9;
    --photo-top: #5d6670;
    --photo-mid: #2c3137;
    --photo-low: #101214;
  }
  * { margin: 0; padding: 0; box-sizing: border-box; }
  html, body { width: 1200px; height: 3000px; overflow: hidden; }
  body {
    background: var(--canvas);
    font-family: "Roboto", Arial, sans-serif;
    position: relative;
  }
  .page {
    position: absolute;
    left: 280px;
    width: 640px;
    height: 905px;
    background: var(--paper);
    overflow: hidden;
    box-shadow: 0 14px 34px rgba(0,0,0,0.18);
  }
  .front-cover { top: 260px; }
  .back-cover { top: 1560px; }
  .page-shapes { position: absolute; inset: 0; width: 640px; height: 905px; }

  .brand {
    position: absolute;
    top: 56px;
    right: 48px;
    text-align: right;
    color: var(--ink);
  }
  .brand-name {
    font-weight: 300;
    font-size: 26px;
    letter-spacing: 0.02em;
    display: flex;
    align-items: center;
    gap: 10px;
    justify-content: flex-end;
  }
  .brand-mark { width: 10px; height: 10px; background: var(--green); }
  .brand-tagline {
    font-weight: 300;
    font-size: 15px;
    letter-spacing: 0.04em;
    margin-top: 2px;
    margin-right: 20px;
    color: #333;
  }

  .cover-headline {
    position: absolute;
    left: 60px;
    top: 565px;
    font-weight: 300;
    font-size: 31px;
    line-height: 1.3;
    color: var(--white);
  }
  .cover-headline .accent { color: var(--green); }

  .back-quote {
    position: absolute;
    left: 62px;
    top: 138px;
    width: 460px;
    font-size: 16.5px;
    line-height: 1.4;
    color: var(--ink);
  }
  .contact {
    position: absolute;
    left: 62px;
    top: 635px;
    font-size: 11.5px;
    line-height: 1.6;
    color: var(--muted);
  }
  .contact-address { margin-bottom: 26px; }
  .contact-lines li { list-style: none; display: flex; align-items: center; gap: 6px; }
  .contact-lines svg { width: 10px; height: 10px; fill: var(--muted); }
  .contact-web {
    margin-top: 26px;
    color: var(--green);
    font-weight: 500;
  }
</style>
</head>
<body>

<section class="page front-cover">
  <svg class="page-shapes" viewBox="0 0 640 905" aria-hidden="false">
    <defs>
      <linearGradient id="earth-tones" x1="0" y1="0" x2="0.35" y2="1">
        <stop offset="0" stop-color="#8a939c"/>
        <stop offset="0.25" stop-color="var(--photo-top)"/>
        <stop offset="0.6" stop-color="var(--photo-mid)"/>
        <stop offset="1" stop-color="var(--photo-low)"/>
      </linearGradient>
    </defs>
    <polygon points="0,244 640,186 640,905 0,905" fill="url(#earth-tones)"
      role="img" aria-label="Foto: Blick aus dem Orbit auf die Erde mit Wolkendecke, rechts oben ein Teil einer Raumstation"/>
  </svg>

  <div class="brand">
    <div class="brand-name">Hollweck &amp; Feist <span class="brand-mark"></span></div>
    <div class="brand-tagline">project consulting</div>
  </div>

  <h1 class="cover-headline">
    <span class="accent">Softwarelösungen</span> für<br>
    digitale Unternehmens-<br>
    prozesse
  </h1>
</section>

<section class="page back-cover">
  <svg class="page-shapes" viewBox="0 0 640 905" aria-hidden="true">
    <polygon points="0,325 640,254 640,905 0,905" fill="var(--dark)"/>
  </svg>

  <p class="back-quote">»Ihilique sumquasped mo in nonsequi consenducit adisimil ipidebi scimus ullaccusa et quas voluptatur, nonsequiam quodipi cidenie ntiatur. Qui autem qui.«</p>

  <address class="contact" style="font-style:normal">
    <div class="contact-address">
      Hollweck &amp; Feist GmbH<br>
      Lindenhof-Allee 14<br>
      80331 München
    </div>
    <ul class="contact-lines">
      <li><svg viewBox="0 0 10 10"><path d="M2 0.5 L3.8 2.6 L2.9 3.8 Q4 6 6.2 7.1 L7.4 6.2 L9.5 8 L8.3 9.5 Q4.5 9.2 2 6.5 Q0.4 4 0.6 1.6 Z"/></svg>+49 89 512 67 40-0</li>
      <li><svg viewBox="0 0 10 10"><rect x="2.5" y="0.5" width="5" height="3"/><rect x="0.5" y="3.5" width="9" height="4.5"/><rect x="2.5" y="7" width="5" height="2.5"/></svg>+49 89 512 67 40-999</li>
      <li><svg viewBox="0 0 10 10"><path d="M0.5 2 H9.5 V8.5 H0.5 Z M0.5 2 L5 5.5 L9.5 2" stroke="var(--dark)" stroke-width="0.8"/></svg>service@hollweckfeist.de</li>
    </ul>
    <div class="contact-web">www.hollweckfeist.de</div>
  </address>
</section>

</body>
</html>
```